new business card and logo for a high end Automotive repair and performance shop

Need to update our design for our business cards. New address, and want a new look. I'll upload some pics of our current card. We are a high end auto repair/tuning shop. New address will be 5192 W. Larkfield Ave Brayford, T.X. 70418. I do have the vector files if needed. The logo would have a similar design. Love the look of carbon fiber, and brushed aluminum, although may have issues showing the texture of the material due to dpi restrictions during card printing. Also the logo would have to be easily printed on shirts, and for embroidery. Thanks, and good luck.

www.motor-zenith.example

Target Market(s)

High end automotive repair, dealership alternative.

Industry/Entity Type

Automotive

Contact Information for Business Card

MOTORZENITH
5192 W. LARKFIELD AVE
BRAYFORD, T.X. 70418
PH 555-307-9261
FAX 555-307-4470
EMAIL INFO@MOTOR-ZENITH.EXAMPLE

Logo Text

MotorZenith

Font styles to use
Sans Serif

Requirements
Must have
• name, address, description that was uploaded.
Nice to have
• maybe some brands i.e. vardo, orvex, Talvani, qrt, solvanta, dovik etc. not necessary. simple is good, like the look of carbon fiber, brushed aluminum.
Should not have
• open to all suggestions.

```html
<!DOCTYPE html>
<html lang="en">
<head>
<meta charset="utf-8">
<title>MotorZenith Business Card</title>
<link rel="stylesheet" href="https://fonts.googleapis.com/css2?family=Open+Sans:wght@400;600;700&display=swap">
<style>
  :root {
    --canvas: #2b2725;
    --card-black: #0d0d0d;
    --card-red: #cc1625;
    --brand-red: #d01c2a;
    --text-light: #e9e9e9;
    --white: #ffffff;
    --divider: #4a1a1e;
  }
  * { margin: 0; padding: 0; box-sizing: border-box; }
  html, body { width: 1200px; height: 900px; overflow: hidden; }
  body {
    background: var(--canvas);
    font-family: "Open Sans", Arial, sans-serif;
    position: relative;
  }
  .card {
    position: absolute;
    top: 285px;
    width: 540px;
    height: 320px;
    border-radius: 4px;
    box-shadow: 0 10px 30px rgba(0,0,0,.45);
  }
  .card-front { left: 40px; background: var(--card-black); color: var(--text-light); }
  .card-back { left: 620px; background: var(--card-red); color: var(--white); }

  .brand {
    position: absolute;
    display: flex;
    align-items: center;
    gap: 12px;
    font-weight: 700;
    letter-spacing: 3px;
  }
  .card-front .brand { top: 70px; left: 120px; font-size: 40px; color: var(--brand-red); }
  .card-front .brand-dot { width: 14px; height: 14px; border-radius: 50%; background: var(--brand-red); }
  .card-back .brand { top: 100px; left: 0; right: 0; justify-content: center; font-size: 46px; color: var(--white); }
  .card-back .brand-dot { width: 16px; height: 16px; border-radius: 50%; background: var(--white); }

  .owner {
    position: absolute;
    top: 170px;
    right: 300px;
    text-align: right;
    font-size: 15px;
    line-height: 1.45;
    white-space: nowrap;
  }
  .owner-name { color: var(--brand-red); font-weight: 700; font-size: 18px; }
  .owner-title { margin-bottom: 6px; }

  .divider {
    position: absolute;
    top: 160px;
    left: 258px;
    width: 1px;
    height: 110px;
    background: var(--divider);
  }

  .contact-list {
    position: absolute;
    top: 160px;
    left: 276px;
    list-style: none;
    font-size: 14px;
    line-height: 1.9;
    white-space: nowrap;
  }
  .contact-list li { display: flex; align-items: center; gap: 9px; }
  .contact-icon { width: 12px; height: 12px; flex: none; fill: var(--brand-red); }

  .tagline {
    position: absolute;
    top: 205px;
    left: 60px;
    right: 60px;
    text-align: center;
    font-size: 13px;
    font-weight: 600;
    line-height: 1.45;
    text-transform: uppercase;
    letter-spacing: .3px;
  }
</style>
</head>
<body>
  <section class="card card-front">
    <div class="brand"><span class="brand-dot"></span>MOTORZENITH</div>

    <div class="owner">
      <div class="owner-name">Dale Carver</div>
      <div class="owner-title">owner</div>
      <div>5192 W. Larkfield Ave unit 7</div>
      <div>Brayford, T.X. 70418</div>
    </div>

    <div class="divider"></div>

    <ul class="contact-list">
      <li>
        <svg class="contact-icon" viewBox="0 0 24 24" aria-hidden="true"><path d="M6.6 10.8a15 15 0 0 0 6.6 6.6l2.2-2.2c.3-.3.7-.4 1-.2 1.1.4 2.3.6 3.6.6.6 0 1 .4 1 1V20c0 .6-.4 1-1 1A17 17 0 0 1 3 4c0-.6.4-1 1-1h3.5c.6 0 1 .4 1 1 0 1.3.2 2.5.6 3.6.1.3 0 .7-.2 1z"/></svg>
        1-555-307-9261
      </li>
      <li>
        <svg class="contact-icon" viewBox="0 0 24 24" aria-hidden="true"><path d="M6 2h12v6H6zM3 9h18a1 1 0 0 1 1 1v8h-4v4H6v-4H2v-8a1 1 0 0 1 1-1zm5 7v4h8v-4z"/></svg>
        1-555-307-4470
      </li>
      <li>
        <svg class="contact-icon" viewBox="0 0 24 24" aria-hidden="true"><path d="M2 5h20v14H2zm2 2v.5l8 5 8-5V7z"/></svg>
        info@motor-zenith.example
      </li>
      <li>
        <svg class="contact-icon" viewBox="0 0 24 24" aria-hidden="true"><circle cx="12" cy="12" r="10"/></svg>
        www.motor-zenith.example
      </li>
    </ul>
  </section>

  <section class="card card-back">
    <div class="brand"><span class="brand-dot"></span>MOTORZENITH</div>
    <p class="tagline">Specializing in Asian, European, and Domestic<br>vehicle repair, service, fabrication, and<br>performancr</p>
  </section>
</body>
</html>
```